The Restful Airway & Jaw Clinic of Larchmont
Corinne T. Valdez D.D.S., Pharm.D, LVIF
The Restful Airway & Jaw Clinic of Larchmont - Health
Creative Brief
Use specific fonts
Use what works the best in your design
Professional
The Restful Airway & Jaw Clinic of LM
37 Gorse Lane Fenwick, OR 97431
cvaldezdds@quillmail.net
I like colors in Greens and complimentary colors. I prefers logos that are more abstract in design with elegant (not cursive) fonts. I am drawn to logos which look like abstract "faces" or "symbols". I treat many patients who are in pain, and would like my logo and design to exude a sense of well-being and serenity. I would like the logo to focus more on the "sleep" aspect (perhaps an abstract of a person sleeping?). Please no teeth or dental symbols! Please use several complimentary colors in the design. You may abbreviate "Larchmont" to "LM" if it works better in your design

```html
<!DOCTYPE html>
<html lang="en">
<head>
<meta charset="utf-8">
<title>The Restful Airway &amp; Jaw Clinic of Larchmont – Business Card</title>
<link rel="stylesheet" href="https://fonts.googleapis.com/css2?family=Source+Sans+3:ital,wght@0,400;0,700;1,400&display=swap">
<style>
  :root {
    --backdrop: #e9ebe6;
    --card-green-deep: #6dbb3c;
    --card-green-light: #a6d843;
    --swirl-yellow: #d8ea3a;
    --swirl-soft: rgba(222, 236, 70, 0.55);
    --ink: #141a10;
    --ink-soft: #2c3a1e;
    --contact-text: #f4f9e6;
  }
  * { box-sizing: border-box; margin: 0; padding: 0; }
  html, body {
    width: 1200px; height: 840px; overflow: hidden;
    background: var(--backdrop);
    font-family: "Source Sans 3", "Myriad Pro", Arial, sans-serif;
  }
  .canvas { position: relative; width: 1200px; height: 840px; }

  .card {
    position: absolute;
    width: 580px; height: 331px;
    background: linear-gradient(135deg, var(--card-green-deep) 0%, var(--card-green-light) 55%, var(--card-green-deep) 100%);
    box-shadow: 0 6px 18px rgba(0,0,0,0.18);
    overflow: hidden;
  }
  .card--front { left: 70px; top: 80px; }
  .card--back  { left: 550px; top: 450px; }

  .swirl-area {
    position: absolute;
    border-radius: 50%;
    background: radial-gradient(ellipse at center, var(--swirl-soft) 0%, rgba(216,234,58,0.25) 50%, rgba(216,234,58,0) 72%);
  }
  .card--front .swirl-area--top-right { right: -40px; top: 40px; width: 280px; height: 280px; }
  .card--front .swirl-area--center { left: 150px; top: 90px; width: 300px; height: 220px; }
  .card--back .swirl-area--left { left: -40px; top: 40px; width: 320px; height: 240px; }
  .card--back .swirl-area--top-right { right: -30px; top: -50px; width: 260px; height: 220px; }

  .clinic-title {
    position: absolute;
    font-weight: 700;
    color: var(--ink);
    letter-spacing: -0.2px;
    line-height: 1.1;
  }
  .card--front .clinic-title { left: 22px; top: 22px; font-size: 22px; }
  .card--back .clinic-title { left: 30px; top: 150px; width: 520px; font-size: 22px; text-align: center; }

  .practitioner {
    position: absolute;
    right: 22px; top: 78px;
    text-align: right;
    color: var(--ink-soft);
  }
  .practitioner__clinic { font-weight: 700; font-size: 15px; color: var(--ink); }
  .practitioner__name { font-style: italic; font-size: 13px; margin-top: 2px; }

  .contact {
    position: absolute;
    left: 22px; bottom: 24px;
    list-style: none;
    color: var(--contact-text);
    font-size: 15px;
    line-height: 1.3;
  }
</style>
</head>
<body>
<main class="canvas">

  <section class="card card--front" aria-label="Business card front">
    <div class="swirl-area swirl-area--center" role="img" aria-label="Soft yellow-green decorative swirl flourishes"></div>
    <div class="swirl-area swirl-area--top-right" role="img" aria-label="Yellow-green decorative swirl flourishes"></div>

    <h1 class="clinic-title">The Restful Airway &amp; Jaw Clinic of Larchmont</h1>

    <div class="practitioner">
      <p class="practitioner__clinic">The Restful Airway &amp; Jaw Clinic of LM</p>
      <p class="practitioner__name">Corinne T. Valdez D.D.S., Pharm.D, LVIF</p>
    </div>

    <ul class="contact">
      <li>37 Gorse Lane</li>
      <li>Fenwick, OR 97431</li>
      <li>Phone : 541-555-0182</li>
      <li>Fax : 541-555-0197</li>
      <li>Email : cvaldezdds@quillmail.net</li>
    </ul>
  </section>

  <section class="card card--back" aria-label="Business card back">
    <div class="swirl-area swirl-area--left" role="img" aria-label="Yellow-green decorative swirl flourishes"></div>
    <div class="swirl-area swirl-area--top-right" role="img" aria-label="Yellow-green decorative swirl flourishes"></div>

    <h2 class="clinic-title">The Restful Airway &amp; Jaw Clinic of Larchmont</h2>
  </section>

</main>
</body>
</html>
```